■依頼の目的/概要
ビジネス本の表紙デザインをお願いします。

■本の内容
・起業初期の起業家、または副業で月収入10万円UPしたい方向けの、
77のWEBのアドバイス(テクニック)をまとめた本です。

■デザイン要望
どちらかというと、30~50代女性起業家向けです。
女性のイラストが入ると嬉しいです。

その他何かご不明な点がございましたら、お気軽にご質問下さい。
よろしくお願いいたします。

■プレセントの記載をお願いします。
①何が足りないかすぐ分かる!
WEBチェックシート

②1年で1万人フォロワーを達成した
Plumoraフォロワー増やしのコツ

③最短で成功へ向かう無料コンサル

女性らしい優しい雰囲気で、誰からも愛されるデザインと感じました。

この度はご応募頂き、誠にありがとうございました!

どのデザインも素敵で、本当に迷いました。
修正していただいた方には、親切に対応して頂き心より感謝しております。

皆様の益々のご活躍を祈念しております。
今回は本当に有難うございました。

```html
<!DOCTYPE html>
<html lang="ja">
<head>
<meta charset="UTF-8">
<title>毎月収入10万円UPしたいあなたに贈る! 知っておくべきWEBテクニック77のポイント</title>
<link rel="stylesheet" href="https://fonts.googleapis.com/css2?family=Noto+Serif+JP:wght@700;900&family=Noto+Sans+JP:wght@500;700;900&display=swap">
<style>
  :root {
    --pink: #e8407a;
    --pink-soft: #f6c9d8;
    --pink-mist: #fbe6ee;
    --navy: #1f2a44;
    --ink: #2a2a33;
    --paper: #ffffff;
    --room-light: #eef0ee;
    --room-mid: #c9d0cc;
    --sofa: #5e7f86;
  }
  * { margin: 0; padding: 0; box-sizing: border-box; }
  html, body { width: 750px; height: 1200px; overflow: hidden; background: var(--paper); }
  .cover {
    position: relative; width: 750px; height: 1200px; overflow: hidden;
    background: linear-gradient(160deg, var(--pink-mist) 0%, var(--paper) 38%, var(--paper) 100%);
    font-family: "Noto Sans JP", sans-serif; color: var(--ink);
  }
  .photo {
    position: absolute; left: 0; top: 470px; width: 750px; height: 730px;
    background:
      radial-gradient(ellipse 260px 300px at 470px 380px, #d8c2b4 0%, rgba(216,194,180,0) 70%),
      linear-gradient(180deg, rgba(255,255,255,0) 0%, var(--room-light) 18%, var(--room-mid) 62%, var(--sofa) 100%);
  }
  .vt { position: absolute; writing-mode: vertical-rl; white-space: nowrap; }
  .up { text-orientation: upright; }
  .tcy { text-combine-upright: all; }
  .income-box {
    left: 642px; top: 18px; width: 98px; height: 520px;
    border: 4px solid var(--navy); background: var(--paper);
    display: flex; align-items: center; justify-content: center;
    font-weight: 900; font-size: 48px; color: var(--navy); line-height: 1;
  }
  .income-box .num { color: var(--pink); font-size: 62px; }
  .lead { left: 574px; top: 42px; font-family: "Noto Serif JP", serif; font-weight: 900; font-size: 50px; color: var(--navy); line-height: 1; }
  .title {
    font-family: "Noto Serif JP", serif; font-weight: 900; font-size: 66px; color: var(--pink);
    line-height: 1; letter-spacing: -2px;
  }
  .title-1 { left: 486px; top: 40px; }
  .title-2 { left: 398px; top: 80px; }
  .count { position: absolute; left: 28px; top: 90px; font-family: "Noto Serif JP", serif; font-weight: 900; font-size: 210px; line-height: 1; color: var(--navy); letter-spacing: -14px; }
  .count-label { left: 196px; top: 255px; font-family: "Noto Serif JP", serif; font-weight: 900; font-size: 40px; color: var(--navy); line-height: 1; }
  .gift-badge {
    position: absolute; left: 12px; top: 320px; width: 168px; height: 168px; border-radius: 50%;
    background: var(--pink-soft); border: 4px solid var(--paper);
    display: flex; flex-direction: column; align-items: center; justify-content: center;
    font-weight: 900; color: var(--navy); line-height: 1.25; font-size: 24px; text-align: center;
  }
  .gift-badge .big { color: var(--pink); font-size: 38px; }
  .gifts { position: absolute; left: 196px; top: 585px; display: flex; flex-direction: row-reverse; gap: 10px; }
  .gift {
    writing-mode: vertical-rl; font-weight: 700; font-size: 26px; line-height: 1.3;
    color: var(--navy); background: rgba(255,255,255,0.55); padding: 6px 2px; white-space: nowrap;
  }
  .gift .mark {
    display: inline-block; text-combine-upright: all; background: var(--navy); color: var(--paper);
    border-radius: 50%; width: 28px; height: 28px; line-height: 28px; text-align: center;
    font-size: 18px; margin-bottom: 6px;
  }
  .author {
    position: absolute; left: 440px; top: 1138px; width: 310px; height: 48px;
    background: rgba(255,255,255,0.85);
    font-family: "Noto Serif JP", serif; font-weight: 700; font-size: 28px; color: var(--navy);
    display: flex; align-items: center; justify-content: center; letter-spacing: 2px;
  }
  .author small { font-size: 22px; margin-left: 10px; }
  .dots { position: absolute; left: 232px; top: 1160px; }
</style>
</head>
<body>
<div class="cover">
  <div class="photo" role="img" aria-label="明るい部屋のソファで、ノートパソコンを膝にのせて微笑む女性の写真"></div>

  <div class="vt income-box"><span>毎月収入<span class="num tcy">10</span>万円<span class="up">UP</span></span></div>
  <div class="vt lead">したいあなたに贈る!</div>
  <h1>
    <span class="vt title title-1">知っておくべき</span>
    <span class="vt title title-2"><span class="up">WEB</span>テクニック</span>
  </h1>
  <div class="count">77</div>
  <div class="vt count-label">のポイント</div>

  <div class="gift-badge"><span><span class="big">3</span>つの</span><span>読者</span><span>プレゼント</span></div>

  <div class="gifts">
    <p class="gift"><span class="mark">1</span>何が足りないかすぐ分かる!<br><span class="up">WEB</span>チェックシート</p>
    <p class="gift"><span class="mark">2</span>1年で1万人フォロワーを達成した<br>Plumoraフォロワー増やしのコツ</p>
    <p class="gift"><span class="mark">3</span>最短で成功へ向かう無料コンサル</p>
  </div>

  <svg class="dots" width="200" height="8" viewBox="0 0 200 8" aria-hidden="true">
    <line x1="4" y1="4" x2="196" y2="4" stroke="#ffffff" stroke-width="6" stroke-linecap="round" stroke-dasharray="0 14"/>
  </svg>
  <div class="author">花村ゆりえ<small>著</small></div>
</div>
</body>
</html>
```